V.Lumo Gin - Bottle label Design

We are manufacturers of Gin in South Africa.
The name of our Gin is V.Lumo Gin with Q standing for Velumzi, a Xhosa Village in the region of Eastern Cape.

We would like our brand to depict the following (really the focus of Gold on it)
> Prosperity of the place
> Wealth of the place, land, material or in the people
> Gold rush, potential, hope

As the brand matures, we would like to have campaigns with it. See ideas below:
> V.Lumo Premium
> Black gold edition
Limited edition will be released every year
- V.Lumo estopini (location)
- V.Lumo emlanjeni (location)

> Each batch of bottles with focus on a specific area/location in Velumzi. One that is known and will be highlighted on the map design of the bottle.
Bottles based on landmarks in Velumzi and landmark design in the Big V.

Below we tried but we are not where we really want to be in terms of Gin Bottle elegance.

Target Market(s)

Target market is the young crowd. Young Xhosa men and women working really hard to get their goals. Positive thinkers. Elegant. Fresh. Bold. Age from 24 to 45. People who enjoy quality products.

Industry/Entity Type

Beverage Industry. Craft Gin.

Font styles to use
Sans Serif
Decorative

Colors
FFF300
FFF600
FEFA6F
FFFEC7
FFFEE8
FFC000
F8CF3A
FAE287
FDF2CF
FEFAEE

Requirements
Must have
• Gold colour as a theme. Try and make the background textured.

```html
<!DOCTYPE html>
<html lang="en">
<head>
<meta charset="utf-8">
<title>V.Lumo Gin – Bottle Label</title>
<link href="https://fonts.googleapis.com/css2?family=Poiret+One&family=Pathway+Gothic+One&display=swap" rel="stylesheet">
<style>
  :root {
    --canvas: #e8e5d9;
    --label: #ffffff;
    --ink: #1d1d1d;
    --ornament: #6b3d0e;
    --gold: #c9a02c;
    --rule: #3a3a3a;
    --map: #f4f3f5;
  }
  * { margin: 0; padding: 0; box-sizing: border-box; }
  html, body {
    width: 1200px; height: 1200px; overflow: hidden;
    background: var(--canvas);
  }
  .canvas { position: relative; width: 1200px; height: 1200px; }
  .label {
    position: absolute; left: 121px; top: 217px;
    width: 958px; height: 766px; background: var(--label);
  }
  .ornament-band {
    position: absolute; left: 44px; width: 870px; height: 41px;
    background: linear-gradient(90deg, #7a4a18, #5e340b 50%, #7a4a18);
    opacity: .85;
  }
  .ornament-band.top { top: 35px; }
  .ornament-band.bottom { top: 707px; }
  .landscape {
    position: absolute; left: 43px; top: 98px; width: 871px; height: 341px;
    background: linear-gradient(180deg, #fbf6d8 0%, #e6c680 35%, #b98a3c 55%, #efe3a8 75%, #fff36a 100%);
  }
  .brand {
    position: absolute; left: 167px; top: 308px; height: 210px;
    display: flex; align-items: center; gap: 22px;
  }
  .brand-mark {
    width: 192px; height: 192px; border-radius: 50%;
    background: var(--gold); border: 6px solid var(--label);
  }
  .brand-name {
    font-family: "Poiret One", sans-serif; font-size: 118px; line-height: 1;
    color: var(--ink); background: var(--label); padding: 0 14px 6px;
    margin-top: 58px;
  }
  .area-map {
    position: absolute; left: 44px; top: 467px; width: 224px; height: 221px;
    background: var(--map);
  }
  .facts {
    position: absolute; left: 45px; top: 551px; width: 870px; height: 139px;
    border: 2px dotted var(--rule);
    display: grid; grid-template-columns: 292px 1fr 1fr; grid-template-rows: 70px 1fr;
  }
  .facts > div { display: flex; align-items: center; justify-content: center; }
  .product {
    grid-row: 1 / 3; border-right: 2px dotted var(--rule);
    font-family: "Poiret One", sans-serif; font-size: 110px; color: var(--ink);
    letter-spacing: 4px; padding-top: 8px;
  }
  .tagline {
    grid-column: 2 / 4; border-bottom: 2px dotted var(--rule);
    font-family: "Pathway Gothic One", sans-serif; font-size: 31px;
    letter-spacing: 2px; color: var(--ink);
  }
  .strength, .volume {
    font-family: "Pathway Gothic One", sans-serif; font-size: 32px; color: var(--ink);
  }
  .strength { border-right: 2px dotted var(--rule); }
</style>
</head>
<body>
<div class="canvas">
  <section class="label">
    <div class="ornament-band top" role="img" aria-label="Row of brown Xhosa-inspired geometric ornaments"></div>
    <div class="landscape" role="img" aria-label="Gold-toned sketch of the Velumzi village landscape with hills, houses and fences"></div>
    <div class="area-map" role="img" aria-label="Faint street map of the village"></div>
    <div class="brand">
      <div class="brand-mark"></div>
      <div class="brand-name">V.Lumo</div>
    </div>
    <div class="facts">
      <div class="product">GIN</div>
      <div class="tagline">Our Golden Gift from Velumzi to the World</div>
      <div class="strength">43% alc.vol.</div>
      <div class="volume">750 ml</div>
    </div>
    <div class="ornament-band bottom" role="img" aria-label="Row of brown Xhosa-inspired geometric ornaments"></div>
  </section>
</div>
</body>
</html>
```